2 Billboard Designs

R & T Tooling is expanding and have purchased 4 billboards. We are looking to have two separate billboard designs and would like 4 options per billboard created to choose from. We do have brand guidelines that can be provided as well as examples of our goal / intent for design.

3 of the billboards are out of state and located about 35 miles from facility and will need to indicate that a shorter commute could be available by choosing to work for us. The 2nd design is a billboard located just 1 mile from our exit and 2 miles from facility and we are hoping to call that out within the advertisement so people know they are just 1 mile (this exit) from being able to apply / our location.

Also looking for any ideas to make more snazzy. I included some of our thoughts but it's just kind of bland. No pazzass or capturing of attention and hoping to have some help with that as well as the graphic aspect of a nicer deliverable in terms of showcasing our brand and company. (I included some pictures of our building to try and demonstrate what I mean.

Please note that I was not able to upload the picture files that we had professionally done that could be used on this project as the upload size was too small.

Target Market(s)

Job Applicants Interest (CNC Machinist, Engineers etc)

Industry/Entity Type

Aerospace, Defense, Medical

Font styles to use
Sans Serif

Colors
0054AA
0677BA
7BADD7
CADEEF
E8F1F8
FFC000
F8CF3A
FAE287
FDF2CF
FEFAEE

Requirements
Must have
• 2 Separate Billboard Designs (options to choose from for both) . Branded guidelines at the standard of our organization. World Class: www.randttooling.example
Nice to have
• Creative Content that is able to uniquely spark interest and make us stand out.

```html
<!DOCTYPE html>
<html lang="en">
<head>
<meta charset="utf-8">
<title>R &amp; T Tooling – Billboard</title>
<link rel="stylesheet" href="https://fonts.googleapis.com/css2?family=Fira+Sans:wght@700;800&family=Montserrat:wght@500;600;700;800&display=swap">
<style>
  :root {
    --brand-blue: #2a48a8;
    --panel-blue: #1f3592;
    --panel-deep: #18286f;
    --accent-gold: #e0ab10;
    --offer-gold: #f2b51d;
    --ink: #111111;
    --paper: #ffffff;
    --sky-light: #eef4fb;
    --building-grey: #d9dde2;
  }
  * { margin: 0; padding: 0; box-sizing: border-box; }
  html, body { width: 800px; height: 1200px; overflow: hidden; background: var(--paper); }
  .canvas { position: relative; width: 800px; height: 1200px; }
  .billboard {
    position: absolute; left: 20px; top: 448px; width: 760px; height: 304px;
    box-shadow: 0 2px 6px rgba(0,0,0,0.25); overflow: hidden;
    font-family: "Montserrat", sans-serif;
  }
  .hero-zone {
    position: absolute; left: 0; top: 0; width: 461px; height: 304px; overflow: hidden;
  }
  .hero-photo {
    position: absolute; inset: 0;
    background: linear-gradient(100deg, var(--sky-light) 0%, #f1f3f6 40%, var(--building-grey) 75%, #e6e8eb 100%);
  }
  .brand-name {
    position: absolute; left: 20px; top: 32px; height: 44px;
    display: flex; align-items: center; gap: 10px;
    color: var(--brand-blue); font-weight: 600; font-size: 18px; letter-spacing: 1.2px;
  }
  .brand-dot { width: 40px; height: 40px; border-radius: 50%; background: var(--brand-blue); }
  .divider { position: absolute; left: 251px; top: 41px; width: 1.5px; height: 28px; background: #333; }
  .tagline {
    position: absolute; left: 267px; top: 44px;
    font-weight: 700; font-size: 17px; color: var(--ink); letter-spacing: 0.3px;
  }
  .headline {
    position: absolute; left: 20px; top: 95px;
    font-weight: 800; font-size: 34px; line-height: 40px; color: var(--brand-blue); letter-spacing: 0; white-space: nowrap;
  }
  .subhead {
    position: absolute; left: 21px; top: 136px;
    font-weight: 800; font-size: 23px; line-height: 28px; color: var(--ink); white-space: nowrap;
  }
  .cta-band {
    position: absolute; left: 22px; top: 174px; width: 439px; height: 67px;
    background: var(--accent-gold);
    font-family: "Fira Sans", sans-serif;
  }
  .cta-lead { position: absolute; left: 14px; top: 3px; font-weight: 700; font-size: 24px; line-height: 28px; color: var(--brand-blue); }
  .cta-url { position: absolute; left: 14px; top: 27px; font-weight: 800; font-size: 32px; line-height: 36px; color: var(--ink); white-space: nowrap; }
  .location {
    position: absolute; left: 21px; top: 259px;
    font-weight: 600; font-size: 19px; color: var(--ink); letter-spacing: 0.4px; white-space: nowrap;
  }
  .offers-panel {
    position: absolute; left: 461px; top: 0; width: 299px; height: 304px;
    background: linear-gradient(160deg, var(--panel-blue) 0%, #24399a 45%, var(--panel-deep) 100%);
    color: var(--paper);
  }
  .offers-title {
    position: absolute; left: 16px; top: 42px;
    font-weight: 800; font-size: 21px; color: var(--offer-gold);
  }
  .offers-list { position: absolute; left: 16px; top: 78px; list-style: none; }
  .offer {
    display: flex; align-items: flex-start; gap: 10px;
    font-weight: 600; font-size: 15px; line-height: 18px; letter-spacing: 0.5px;
    margin-bottom: 10px; white-space: nowrap;
  }
  .offer svg { flex: none; margin-top: 3px; }
</style>
</head>
<body>
<main class="canvas">
  <section class="billboard">
    <div class="hero-zone">
      <div class="hero-photo" role="img" aria-label="Faded photo of the company's glass-fronted manufacturing building"></div>
      <div class="brand-name"><span class="brand-dot"></span>R&amp;T TOOLING</div>
      <div class="divider"></div>
      <div class="tagline">COMPETITIVE PAY</div>
      <h1 class="headline">COMMUTE TOO LONG?</h1>
      <h2 class="subhead">SEEKING A MACHINING CAREER?</h2>
      <div class="cta-band">
        <div class="cta-lead">Learn More at</div>
        <div class="cta-url">www.randttooling.example</div>
      </div>
      <p class="location">LOCATED IN: LAKEMONT, MICHIGAN</p>
    </div>
    <aside class="offers-panel" role="img" aria-label="Blue panel over a faint photo of machining equipment">
      <h3 class="offers-title">R &amp; T OFFERS:</h3>
      <ul class="offers-list">
        <li class="offer"><svg width="12" height="12" viewBox="0 0 12 12"><rect x="0.75" y="0.75" width="10.5" height="10.5" fill="none" stroke="#f2b51d" stroke-width="1.3"/><path d="M3 6l2 2 4.5-5" fill="none" stroke="#f2b51d" stroke-width="1.3"/></svg><span>AEROSPACE, MEDICAL &amp;<br>DEFENSE MACHINING</span></li>
        <li class="offer"><svg width="12" height="12" viewBox="0 0 12 12"><rect x="0.75" y="0.75" width="10.5" height="10.5" fill="none" stroke="#f2b51d" stroke-width="1.3"/><path d="M3 6l2 2 4.5-5" fill="none" stroke="#f2b51d" stroke-width="1.3"/></svg><span>APPRENTICESHIP PROGRAM</span></li>
        <li class="offer"><svg width="12" height="12" viewBox="0 0 12 12"><rect x="0.75" y="0.75" width="10.5" height="10.5" fill="none" stroke="#f2b51d" stroke-width="1.3"/><path d="M3 6l2 2 4.5-5" fill="none" stroke="#f2b51d" stroke-width="1.3"/></svg><span>ON-THE-JOB TRAINING</span></li>
        <li class="offer"><svg width="12" height="12" viewBox="0 0 12 12"><rect x="0.75" y="0.75" width="10.5" height="10.5" fill="none" stroke="#f2b51d" stroke-width="1.3"/><path d="M3 6l2 2 4.5-5" fill="none" stroke="#f2b51d" stroke-width="1.3"/></svg><span>STATE-OF-THE-ART FACILITY</span></li>
        <li class="offer"><svg width="12" height="12" viewBox="0 0 12 12"><rect x="0.75" y="0.75" width="10.5" height="10.5" fill="none" stroke="#f2b51d" stroke-width="1.3"/><path d="M3 6l2 2 4.5-5" fill="none" stroke="#f2b51d" stroke-width="1.3"/></svg><span>NEW ADVANCED MACHINING<br>TECHNOLOGY</span></li>
        <li class="offer"><svg width="12" height="12" viewBox="0 0 12 12"><rect x="0.75" y="0.75" width="10.5" height="10.5" fill="none" stroke="#f2b51d" stroke-width="1.3"/><path d="M3 6l2 2 4.5-5" fill="none" stroke="#f2b51d" stroke-width="1.3"/></svg><span>COMPETITIVE PAY</span></li>
      </ul>
    </aside>
  </section>
</main>
</body>
</html>
```